crumbs of morning project

I need 2 stickers (lid and side) for a see-through rectangular plastic container that holds a whole, free range chicken.
Updates

CHANGE OF PACKAGING

 

we are unable to source the clear, rectangular, see-throughcontainer in the previously attached file and have to amend our packagingstrategy.

 

 

 

UPDATED STRATEGY:

 

we intend to use one of the 'french style' cardboard typewrap-around stickers as shown in the new attachments I have posted. australiansupermarkets would not accept this type of thin cardboard on its own as is applicablein france and for that reason we intend insert the wrapped-around cardboard stickeredwhole chicken on a poly styrene tray and then placed in a clear plastic cellophanebag with a twisted tie as shown the 'varnot brand' attached file.

 

the other technical requirements (barcode, kilograms, netpricing, etc.) remain the same

 

 

also note:

 

when using our existing 'seal pure' logo, please removethe text:

 

rabbi tovah lindquist haber

potential brand names:

1. crumbs of morning
2. brisk olando

cardboard label needs to be a ' wrap around label' (wrapped, north-south) as shown in the following 
attached files:

'wrap around label'  + 'wrap around label b'

we like the 'brisk olando' FONT and primary yellow background. 

dorvid 

Target Market(s)

free range poultry consumers (GREENIES) jews (seal pure), affluent, up market, product is priced at the premium end of the market

Industry/Entity Type

Plastic

Requirements
Must have
• in order of importance...

LID LABEL STICKER-(see attached photo)
logo name (crumbs of morning)
free range
sanitised with kosher rock salt
extra fresh
long shelf life
kosher certified

SIDE LABEL STICKER- (see attached photo)
country of manufacture
processors contact details
(7 pellbrook lane ashvale west 3290 0487 220 318 www.crumbsofmorning.com.au)
barcode
product description (whole, drumsticks, filets, etc)
kosher status declaration and kosher logo (see attachment)
price per kilogram section
net weight per kilogram section
use by date
total price
refrigeration advise-store below 5degreesC

note:

the whole chicken is wrapped in light BROWN colored butchers paper and tied with a green ribbon. the customer can only see the raw chicken at each end.

```html
<!DOCTYPE html>
<html lang="en">
<head>
<meta charset="utf-8">
<title>Brisk Olando – Whole Chicken Wrap Label</title>
<link rel="stylesheet" href="https://fonts.googleapis.com/css2?family=Arimo:wght@400;700&family=Rye&display=swap">
<style>
  :root {
    --page: #ffffff;
    --frame: #9a9a9a;
    --ink: #231a12;
    --neck: #161616;
    --orange-light: #f7a21b;
    --orange-deep: #e8780f;
    --orange-body: #f09116;
    --ribbon-edge: #f2a900;
    --ribbon-mid: #e9821a;
    --tail-line: #f6dc12;
    --tail-fill: #fbe28a;
    --white: #ffffff;
    --seal: #6e1d1d;
  }
  html, body {
    margin: 0;
    padding: 0;
    width: 1200px;
    height: 900px;
    overflow: hidden;
    background: var(--page);
  }
  .canvas {
    display: block;
    width: 1200px;
    height: 900px;
  }
  .canvas-frame { fill: none; stroke: var(--frame); stroke-width: 2; }
  .label-body { fill: url(#bodyTone); }
  .label-neck { fill: var(--neck); }
  .ribbon-face { fill: url(#ribbonTone); }
  .ribbon-tail { fill: var(--tail-fill); stroke: var(--tail-line); stroke-width: 3; stroke-linejoin: round; }
  .ribbon-text {
    font-family: "Arimo", Arial, sans-serif;
    font-weight: 700;
    fill: var(--ink);
    text-anchor: middle;
  }
  .brand-name {
    font-family: "Rye", Georgia, serif;
    font-size: 46px;
    fill: var(--white);
    text-anchor: middle;
    letter-spacing: 1px;
  }
  .product-band { fill: var(--neck); }
  .product-title {
    font-family: "Arimo", Arial, sans-serif;
    font-weight: 700;
    font-size: 14px;
    fill: var(--white);
    text-anchor: middle;
    letter-spacing: 1px;
  }
  .small-print {
    font-family: "Arimo", Arial, sans-serif;
    font-weight: 700;
    font-size: 10px;
    fill: var(--ink);
  }
  .centered { text-anchor: middle; }
  .seal-name {
    font-family: "Arimo", Arial, sans-serif;
    font-weight: 700;
    font-size: 13px;
    fill: var(--seal);
    text-anchor: middle;
  }
  .info-box { fill: var(--white); }
  .barcode-slot { fill: var(--white); stroke: #d9d9d9; stroke-width: 1; }
  .barcode-word {
    font-family: "Arimo", Arial, sans-serif;
    font-size: 10px;
    fill: var(--ink);
    text-anchor: middle;
  }
</style>
</head>
<body>
<svg class="canvas" viewBox="0 0 1200 900" xmlns="http://www.w3.org/2000/svg">
  <defs>
    <linearGradient id="bodyTone" x1="0" y1="0" x2="0" y2="1">
      <stop offset="0" stop-color="var(--orange-light)"/>
      <stop offset="0.55" stop-color="var(--orange-body)"/>
      <stop offset="1" stop-color="var(--orange-deep)"/>
    </linearGradient>
    <linearGradient id="ribbonTone" x1="0" y1="0" x2="1" y2="0">
      <stop offset="0" stop-color="var(--ribbon-edge)"/>
      <stop offset="0.5" stop-color="var(--ribbon-mid)"/>
      <stop offset="1" stop-color="var(--ribbon-edge)"/>
    </linearGradient>
    <g id="ribbonTails">
      <path class="ribbon-tail" d="M481,49 L462,46 Q478,67 462,88 L481,85 Z"/>
      <path class="ribbon-tail" d="M719,49 L738,46 Q722,67 738,88 L719,85 Z"/>
    </g>
  </defs>

  <rect class="canvas-frame" x="1" y="1" width="1198" height="898"/>

  <!-- label silhouette -->
  <path class="label-body" role="img" aria-label="Orange diamond check pattern on the label body"
        d="M494,452 C478,520 420,640 418,780 L418,822 Q600,868 782,822 L782,780 C780,640 722,520 706,452 Z"/>
  <path class="label-neck" d="M536,80 V425 Q522,442 500,452 V652 H700 V452 Q678,442 658,425 V80 Z"/>

  <!-- claim ribbons -->
  <g class="claim-ribbon">
    <use href="#ribbonTails"/>
    <rect class="ribbon-face" x="480" y="47" width="240" height="40"/>
    <text class="ribbon-text" x="600" y="76" font-size="24">Extra Fresh</text>
  </g>
  <g class="claim-ribbon" transform="translate(0,73)">
    <use href="#ribbonTails"/>
    <rect class="ribbon-face" x="480" y="47" width="240" height="40"/>
    <text class="ribbon-text" x="600" y="76" font-size="24">Free Range</text>
  </g>
  <g class="claim-ribbon" transform="translate(0,147)">
    <use href="#ribbonTails"/>
    <rect class="ribbon-face" x="480" y="47" width="240" height="40"/>
    <text class="ribbon-text" x="600" y="65" font-size="18">Sanitised with</text>
    <text class="ribbon-text" x="600" y="82" font-size="18">Kosher Rock Salt</text>
  </g>
  <g class="claim-ribbon" transform="translate(0,220)">
    <use href="#ribbonTails"/>
    <rect class="ribbon-face" x="480" y="47" width="240" height="40"/>
    <text class="ribbon-text" x="600" y="76" font-size="24">Long Shelf Life</text>
  </g>
  <g class="claim-ribbon" transform="translate(0,295)">
    <use href="#ribbonTails"/>
    <rect class="ribbon-face" x="480" y="47" width="240" height="40"/>
    <text class="ribbon-text" x="600" y="76" font-size="24">Kosher Certified</text>
  </g>

  <!-- brand -->
  <text class="brand-name" x="600" y="578">BRISK</text>
  <text class="brand-name" x="600" y="634">OLANDO</text>

  <!-- product band -->
  <path class="product-band" d="M432,658 H768 L764,681 H428 Z"/>
  <text class="product-title" x="600" y="675">WHOLE CHICKEN</text>
  <text class="small-print centered" x="600" y="694">Product of Australia</text>

  <!-- kosher declaration -->
  <text class="seal-name" x="600" y="724">seal pure</text>
  <text class="small-print centered" x="600" y="743" font-size="9">Kosher Certified</text>

  <!-- pricing box -->
  <rect class="info-box" x="478" y="751" width="244" height="40"/>
  <text class="small-print" x="493" y="767">Best before</text>
  <text class="small-print" x="618" y="767">Net Wt.</text>
  <text class="small-print" x="493" y="783">Price Per KG.</text>
  <text class="small-print" x="618" y="783">Total Price</text>

  <rect class="barcode-slot" x="738" y="722" width="30" height="86"/>
  <text class="barcode-word" transform="translate(756,765) rotate(-90)">barcode</text>

  <text class="small-print centered" x="600" y="806">Store below 5 degree C</text>
  <text class="small-print centered" x="600" y="828">7 Pellbrook Lane Ashvale West 3290.</text>
  <text class="small-print centered" x="600" y="840">www.crumbsofmorning.com.au</text>
</svg>
</body>
</html>
```